Brochure for Harbor Lantern

A unique, dynamic brochure, our website is: www.harborlantern-example.com for more information. Our facebook is linked to it to get a sense of who we are. (Please don't use the pictures from there)

Our colors are black, white, and gray. That is our company colors. Open to color though. (If you can have 4 pages on the inside because of too much content, that is fine, or an extra sheet so it has 4 pages inside)

Our mission at Harbor Lantern is to provide love, encourage dreams, and promote integrity. We have a vested interest in Individual and Staff success. We can be reached. (Would like on the first page)

You will have confidence and trust in us.

Harbor Lantern specializes in working with Individuals with Challenging Behaviors and Psychiatric Mental Illness.

Services: Day Services Including: Job Placement including: Supported Employment, Individual Day Supports, Family Supports, Group Day Supports including Group Employment and Group Day Service; Individual Home Supports, Transportation, and Clinical Behavior Supports. (Would like these bulleted)

We provide assessments (Transitional & Life Skills), intense vocation plans including a clinical component which will help the individual to succeed in the job market and beyond.

Harbor Lantern Believes:
Anything is possible for Individuals and has strategies and sound treatment to see this vision forward.
Harbor Lantern’s Chief Executive Officer is A Doctor of Psychology. Her mission is holistic, clinical and fresh.
Harbor Lantern believes in their individuals who they serve and their employees.

Our Holistic Approach views: Employment is viewed as one component of an individual's life that inter-relates with other key aspects, including social relationships, recreation, and where they live. Non-work activities are considered in relationship to employment. Service are provided so that an individual is able to experience all aspects of community life.

The purpose of employment services is not simply to enable a person with a disability to get a job. Providing quality employment support is able people:
(bulleted)
Reaching their fullest potential.
Becoming fully participating community members.
Having a valued role, with all the rights and responsibilities of living in society.
Experiencing and enjoying all that life has to offer.
Redefinining themselves and their place in the world.

A job is simply a vehicle for these things to happen!

Harbor Lantern Employs an Employment Director who is working hand in hand with the community and local business establishments to secure long-term competitive employment for individuals who are served by us. The right job is out there for our individuals to earn money and enhance quality of living. We match the individual with the job that best fits what they want to do for work.

The feel of our program is different. Our individuals served are happy and free to make choices of what their day looks like, participate in schedule development, learn the necessary skills for life and social skills.

And those who are ready to work…WILL WORK. We have over 10 years of experience. We have a motivated team who are unstoppable in our mission. Let us know how we can help you succeed.

A BFN Qualified Provider for the State of Connecticut and QRW Credentialed through PMT.
Approved Provider for the Office of Lifelong Growth Programs, Autism Division
Private Dollars Accepted as well and Sliding Scale.

Harbor Lantern Corporation
Phone: 860-555-0172
Fax: 860-555-0198
Pending: Non-Profit 501 (c) 3
917 Maple Row
Windsor Locks, CT 06011
www.facebook.com/HarborLantern
www.harborlantern-example.com
info@harborlantern-example.com

• The size of the brochure is a booklet brochure. I should definitely post that in the project. The size would be: an 8/12 sheet of paper folded in half.

```html
<!DOCTYPE html>
<html lang="en">
<head>
<meta charset="utf-8">
<title>Harbor Lantern — Brochure Cover</title>
<link rel="stylesheet" href="https://fonts.googleapis.com/css2?family=Didact+Gothic&family=Tinos:ital,wght@0,400;0,700;1,400&family=Arimo:ital@0;1&display=swap">
<style>
  :root {
    --cover-dark: #231f20;
    --band-white: #ffffff;
    --title-gray: #d9d9d9;
    --text-white: #f4f4f4;
    --photo-glow: #e6e6e6;
    --photo-light: #b8b8b8;
    --photo-mid: #6e6e6e;
    --photo-deep: #2c2c2c;
  }
  html, body {
    margin: 0;
    padding: 0;
    overflow: hidden;
    background: var(--cover-dark);
  }
  .cover {
    position: relative;
    width: 873px;
    height: 1200px;
    overflow: hidden;
    background: var(--cover-dark);
  }
  .cover-art {
    position: absolute;
    inset: 0;
  }
  .brand-name {
    position: absolute;
    left: 62px;
    top: 186px;
    margin: 0;
    font-family: "Didact Gothic", sans-serif;
    font-weight: 400;
    font-size: 78px;
    line-height: 1;
    letter-spacing: 4px;
    color: var(--title-gray);
    white-space: nowrap;
  }
  .brand-url {
    position: absolute;
    right: 203px;
    top: 264px;
    font-family: "Arimo", sans-serif;
    font-size: 14px;
    color: var(--title-gray);
  }
  .tagline {
    position: absolute;
    left: 64px;
    top: 430px;
    margin: 0;
    color: var(--text-white);
    line-height: 0.92;
    white-space: nowrap;
  }
  .tagline-big {
    display: block;
    font-family: "Tinos", serif;
    font-size: 41px;
    letter-spacing: 0.5px;
  }
  .tagline-small {
    display: block;
    font-family: "Arimo", sans-serif;
    font-size: 21px;
    letter-spacing: 0.4px;
  }
  .tagline-note {
    display: block;
    font-family: "Arimo", sans-serif;
    font-style: italic;
    font-size: 19px;
    margin-top: 3px;
    color: #cfcfcf;
  }
  .service-list {
    position: absolute;
    left: 83px;
    top: 1146px;
    margin: 0;
    padding: 0;
    list-style: none;
    display: flex;
    align-items: center;
    font-family: "Tinos", serif;
    font-weight: 700;
    font-size: 15.5px;
    color: var(--text-white);
    white-space: nowrap;
  }
  .service-list li {
    padding: 0 9px;
    border-left: 1.5px solid var(--text-white);
    line-height: 24px;
  }
  .service-list li:first-child {
    padding-left: 0;
    border-left: none;
  }
</style>
</head>
<body>
<main class="cover">
  <svg class="cover-art" width="873" height="1200" viewBox="0 0 873 1200">
    <defs>
      <linearGradient id="photoBase" x1="0" y1="0" x2="1" y2="0">
        <stop offset="0" stop-color="var(--photo-deep)"/>
        <stop offset="0.3" stop-color="var(--photo-mid)"/>
        <stop offset="0.75" stop-color="var(--photo-mid)"/>
        <stop offset="1" stop-color="var(--photo-deep)"/>
      </linearGradient>
      <radialGradient id="photoGlow" cx="640" cy="720" r="330" gradientUnits="userSpaceOnUse" gradientTransform="translate(640 720) scale(0.85 1.35) translate(-640 -720)">
        <stop offset="0" stop-color="var(--photo-glow)"/>
        <stop offset="0.5" stop-color="var(--photo-light)" stop-opacity="0.8"/>
        <stop offset="1" stop-color="var(--photo-light)" stop-opacity="0"/>
      </radialGradient>
      <radialGradient id="photoSide" cx="170" cy="880" r="260" gradientUnits="userSpaceOnUse">
        <stop offset="0" stop-color="#9a9a9a" stop-opacity="0.7"/>
        <stop offset="1" stop-color="#9a9a9a" stop-opacity="0"/>
      </radialGradient>
      <linearGradient id="photoFloor" x1="0" y1="0" x2="0" y2="1">
        <stop offset="0.55" stop-color="#000" stop-opacity="0"/>
        <stop offset="1" stop-color="#000" stop-opacity="0.6"/>
      </linearGradient>
    </defs>
    <path class="photo-frame" d="M0 895 L545 400 Q583 366 622 393 L873 570 V1200 H0 Z" fill="var(--band-white)"/>
    <g role="img" aria-label="Photograph of a smiling professional woman in an office setting">
      <path d="M0 921 L550 422 Q583 392 616 415 L873 596 V1200 H0 Z" fill="url(#photoBase)"/>
      <path d="M0 921 L550 422 Q583 392 616 415 L873 596 V1200 H0 Z" fill="url(#photoSide)"/>
      <path d="M0 921 L550 422 Q583 392 616 415 L873 596 V1200 H0 Z" fill="url(#photoGlow)"/>
      <path d="M0 921 L550 422 Q583 392 616 415 L873 596 V1200 H0 Z" fill="url(#photoFloor)"/>
    </g>
  </svg>

  <h1 class="brand-name">Harbor Lantern</h1>
  <span class="brand-url">www.harborlantern-example.com</span>

  <p class="tagline">
    <span class="tagline-big">REDEFINING</span>
    <span class="tagline-small">CLINICAL TREATMENT FOR</span>
    <span class="tagline-big">SUCCESS</span>
    <span class="tagline-note">OVER 10 YEARS OF EXPERIENCE</span>
  </p>

  <ul class="service-list">
    <li>Day Service</li>
    <li>Individual/Home Consultation</li>
    <li>Organization Consultation</li>
    <li>Individual/Family Support</li>
  </ul>
</main>
</body>
</html>
```